Trade show flier

Need a two sided flier for a trade show that will go with the trade show banner you are designing for us. We have included some information we would like to see o the flier. We do need to work on the content. If you can start a design, we can work on the content. This must be done by 3/12/2018

Target Market(s)

Manufacturing companies

Industry/Entity Type

Trade

```html
<!DOCTYPE html>
<html lang="en">
<head>
<meta charset="utf-8">
<title>Relaywise – Company Profile Flier</title>
<link href="https://fonts.googleapis.com/css2?family=Questrial&family=Montserrat:wght@500;600&display=swap" rel="stylesheet">
<style>
  :root{
    --stage:#262626;
    --paper:#ffffff;
    --band-grey:#e5e5e6;
    --brand-blue:#2c70b6;
    --brand-blue-light:#3b82c4;
    --brand-navy:#1b3557;
    --heading-blue:#2b6cb0;
    --ink:#2e2e2e;
    --ink-soft:#4a4a4a;
    --rule:#b9c3cf;
    --badge:#d9dee5;
  }
  *{box-sizing:border-box;margin:0;padding:0}
  html,body{width:1200px;height:831px;overflow:hidden;background:var(--stage)}
  body{font-family:"Questrial",sans-serif;color:var(--ink);position:relative}

  .page{position:absolute;top:75px;width:483px;height:683px;background:var(--paper);overflow:hidden}
  .page--front{left:84px}
  .page--back{left:633px}

  /* FRONT */
  .front__band{position:absolute;left:0;top:0;width:100%;height:177px;background:var(--band-grey)}
  .brand{position:absolute;top:36px;left:0;width:100%;display:flex;justify-content:center;align-items:center;gap:8px}
  .brand__dot{width:30px;height:30px;border-radius:50%;background:var(--brand-blue)}
  .brand__name{font-size:27px;color:var(--brand-blue);letter-spacing:1px}

  .hero{position:absolute;left:40px;top:97px;width:405px;height:177px;
    background:linear-gradient(180deg,#2a5f9c 0%,var(--brand-blue) 45%,var(--brand-blue-light) 100%);
    color:#fff;text-align:center}
  .hero__title{font-family:"Montserrat",sans-serif;font-weight:600;font-size:33px;letter-spacing:.5px;margin-top:36px}
  .hero__rule{width:290px;height:1px;background:rgba(255,255,255,.6);margin:12px auto 0}
  .hero__established{font-size:11.5px;letter-spacing:1.6px;margin-top:14px}
  .hero__intro{font-size:7.9px;line-height:11.4px;width:300px;margin:7px auto 0}

  .hero__bar{position:absolute;left:40px;top:274px;width:405px;height:14px;background:var(--brand-navy)}
  .hero__photo{position:absolute;left:40px;top:288px;width:405px;height:216px;
    background:linear-gradient(135deg,#9fb8d2 0%,#5e7fa3 40%,#2c4463 75%,#1c2c44 100%)}
  .hero__frame{position:absolute;left:40px;top:504px;width:405px;height:45px;border:1px solid #c9c9c9;border-top:none;
    display:flex;justify-content:center;align-items:center}

  .statement{position:absolute;top:570px;width:170px}
  .statement--vision{left:66px}
  .statement--mission{left:296px}
  .statement__title{font-size:14.6px;letter-spacing:3.2px;color:var(--ink-soft)}
  .statement__text{font-size:7.6px;line-height:14.6px;margin-top:8px;color:var(--ink)}

  /* BACK */
  .back__head{position:absolute;left:53px;top:22px;width:379px;height:44px;border-bottom:1px solid var(--rule)}
  .head-label{position:absolute;color:var(--heading-blue);font-size:11.5px;letter-spacing:.6px;line-height:13.6px}
  .head-label--services{left:33px;bottom:4px}
  .head-label--support{left:226px;bottom:4px}
  .head-icon{position:absolute;bottom:5px}
  .head-icon--services{left:0}
  .head-icon--support{left:204px}

  .list{position:absolute;top:94px;list-style:none;font-size:7.5px;line-height:11.4px}
  .list--services{left:54px;width:170px}
  .list--support{left:257px;width:176px}
  .list li{position:relative;padding-left:8px;margin-bottom:11.4px}
  .list li::before{content:"";position:absolute;left:0;top:4px;width:3px;height:3px;border-radius:50%;background:var(--heading-blue)}

  .pledge{position:absolute;left:51px;top:497px;width:381px;height:69px;
    background:linear-gradient(180deg,#2b5b98 0%,#3c73b4 100%);color:#fff;
    font-size:9.6px;line-height:14.6px;text-align:center;padding:14px 30px 0}
  .partners{position:absolute;left:51px;top:566px;width:381px;height:91px;border:1px solid #c9c9c9;border-top:none}
  .partners__title{position:absolute;left:30px;top:9px;font-size:11.5px;letter-spacing:.4px;color:var(--heading-blue)}
  .partners__grid{position:absolute;left:30px;top:34px;display:grid;grid-template-columns:repeat(4,72px);column-gap:12px;row-gap:10px}
  .partner-badge{height:20px;border-radius:3px;background:var(--badge)}
</style>
</head>
<body>

<section class="page page--front">
  <div class="front__band"></div>
  <div class="brand">
    <span class="brand__dot"></span>
    <span class="brand__name">Relaywise</span>
  </div>

  <div class="hero">
    <h1 class="hero__title">COMPANY PROFILE</h1>
    <div class="hero__rule"></div>
    <p class="hero__established">ESTABLISHED IN 2006</p>
    <p class="hero__intro">Relaywise is a Managed IT Service firm providing exceptional IT consultation and support for businesses in the California with 20 – 1000 employees. Our personable, reliable and professional team empowers our clients to make their IT infrastructure a strategic asset.</p>
  </div>
  <div class="hero__bar"></div>
  <div class="hero__photo" role="img" aria-label="Business professionals reviewing charts on a tablet at a desk"></div>
  <div class="hero__frame">
    <svg width="30" height="24" viewBox="0 0 30 24" fill="none" stroke="#5a8fc8" stroke-width="1.3" stroke-linecap="round" stroke-linejoin="round" aria-hidden="true">
      <path d="M2 8l6-5 5 3 4-2 5 3 6 5"/>
      <path d="M6 12l7 7c1 1 2 1 3 0l7-7"/>
      <path d="M11 14l4 4M14 12l4 4"/>
    </svg>
  </div>

  <div class="statement statement--vision">
    <h2 class="statement__title">OUR VISION</h2>
    <p class="statement__text">To provide a customer<br>experience that provides value<br>and enables technology<br>collaboration effortlessly.</p>
  </div>
  <div class="statement statement--mission">
    <h2 class="statement__title">OUR MISSION</h2>
    <p class="statement__text">Innovative collaboration to<br>improve business process by<br>leveraging technology that<br>empowers organizations to<br>implement a roadmap to success.</p>
  </div>
</section>

<section class="page page--back">
  <div class="back__head">
    <svg class="head-icon head-icon--services" width="22" height="26" viewBox="0 0 22 26" fill="none" stroke="#5a8fc8" stroke-width="1.1" aria-hidden="true">
      <circle cx="11" cy="8" r="5"/>
      <path d="M2 25v-5c0-3 3-5 9-5s9 2 9 5v5z"/>
    </svg>
    <span class="head-label head-label--services">SERVICES</span>
    <svg class="head-icon head-icon--support" width="16" height="20" viewBox="0 0 16 20" fill="none" stroke="#8aa4c4" stroke-width="1" aria-hidden="true">
      <path d="M1 1h9l5 5v13H1z"/>
      <path d="M4 9h8M4 12h8M4 15h8"/>
    </svg>
    <span class="head-label head-label--support">OUR COMMON GROUND<br>MANAGED SERVICES<br>SUPPORT INCLUDE</span>
  </div>

  <ul class="list list--services">
    <li>Managed Services – Proactive support, remediation and maintenance of your technology infrastructure, 24/7.</li>
    <li>Backup and Business Continuity – Secure your data while minimizing downtime.</li>
    <li>Virtualization – Increase IT flexibility and scalability while minimizing hardware resources.</li>
    <li>Voice Collaboration – Voice-over-IP (VOIP) Design and Deployment.</li>
    <li>Cloud Services – Leverage cloud support services for remote access and or business continuity.</li>
    <li>Security Services – Multi-layered approach to addressing your network security.</li>
    <li>Wireless Services – Secure connectivity and centralized management for wireless endpoint devices.</li>
    <li>Procurement Services – Procurement of industry standard business class product.</li>
    <li>Project Collaboration – Strategic technology roadmaps that address company business goals.</li>
    <li>Surveillance Services - Intelligent network security video solutions.</li>
  </ul>

  <ul class="list list--support">
    <li>Team of industry certified Network Engineers</li>
    <li>Remote support (Weekdays 7am – 6pm)</li>
    <li>Onsite support (Weekdays 7am – 6pm)</li>
    <li>24x7 network monitoring and remediation</li>
    <li>Daily proactive maintenance</li>
    <li>Managed antivirus software</li>
    <li>Managed ransomware protection</li>
    <li>Ticketing portal to track open tickets and resolutions</li>
    <li>Vendor management</li>
    <li>Network Documentation Management</li>
    <li>Software License Management</li>
    <li>Technology procurement</li>
    <li>Monitoring of existing backup systems and data recovery</li>
    <li>Business continuity planning</li>
    <li>Network and data security planning and testing</li>
    <li>Quarterly IT meetings</li>
  </ul>

  <p class="pledge">We provide a great customer service experience with a simplified, cost-effective approach to IT that leverages certified technical professionals with industry standard skills and knowledge.</p>

  <div class="partners">
    <h3 class="partners__title">OUR TECHNOLOGY PARTNERS</h3>
    <div class="partners__grid">
      <span class="partner-badge"></span><span class="partner-badge"></span><span class="partner-badge"></span><span class="partner-badge"></span>
      <span class="partner-badge"></span><span class="partner-badge"></span><span class="partner-badge"></span><span class="partner-badge"></span>
    </div>
  </div>
</section>

</body>
</html>
```